Plastic Business Cards

I am looking for a plastic business card that matches the theme of my company.

Attached will be logo and template to Prindlecraft for printing.

On card please include the following information:

Logo
612-437-9158 Call or Text
www.GlintvaleCo.com

Window Cleaning
Gutter Cleaning & Covers
Christmas Lighting

200+ 5 Star Reviews

```html
<!DOCTYPE html>
<html lang="en">
<head>
<meta charset="utf-8">
<title>Glintvale Window Cleaning – Business Cards</title>
<link href="https://fonts.googleapis.com/css2?family=Montserrat:wght@400;500&family=Oswald:wght@500;600&display=swap" rel="stylesheet">
<style>
  :root {
    --navy: #0b2456;
    --navy-deep: #061a44;
    --navy-light: #1a3a78;
    --sky: #2a9ad6;
    --ice: #bfe9fb;
    --lime: #8fd11f;
    --white: #ffffff;
    --paper: #f3f4f5;
    --backdrop: #d9dbde;
  }
  * { box-sizing: border-box; margin: 0; padding: 0; }
  html, body { width: 1200px; height: 1200px; overflow: hidden; }
  body {
    background: var(--backdrop);
    font-family: "Montserrat", sans-serif;
    position: relative;
  }
  .card {
    position: absolute;
    left: 150px;
    width: 900px;
    height: 514px;
    border-radius: 34px;
    overflow: hidden;
    box-shadow: 0 10px 30px rgba(0,0,0,0.25);
  }
  /* Front */
  .card-front { top: 60px; background: radial-gradient(circle at 50% 35%, var(--white), var(--paper)); }
  .front-stripe {
    position: absolute; left: 0; right: 0; top: 250px; height: 12px;
    background: var(--lime);
  }
  .front-panel {
    position: absolute; left: 0; right: 0; top: 274px; bottom: 0;
    background: radial-gradient(circle at 40% 0%, var(--navy-light), var(--navy) 60%, var(--navy-deep));
  }
  .brand {
    position: absolute; left: 0; right: 0;
    display: flex; align-items: center; justify-content: center; gap: 18px;
    font-family: "Oswald", sans-serif; font-weight: 600;
    text-transform: uppercase; letter-spacing: 2px;
  }
  .brand-dot { border-radius: 50%; background: var(--lime); flex: none; }
  .card-front .brand { top: 70px; color: var(--navy); font-size: 64px; }
  .card-front .brand-dot { width: 46px; height: 46px; }
  .person {
    position: absolute; left: 70px; top: 110px;
    border-left: 4px solid var(--sky); padding-left: 18px;
  }
  .person-name { color: var(--sky); font-size: 40px; font-weight: 500; letter-spacing: 1px; line-height: 1.1; }
  .person-role { color: var(--white); font-size: 22px; font-weight: 400; letter-spacing: 1px; margin-top: 4px; }
  .divider {
    position: absolute; left: 470px; top: 40px; width: 1px; height: 150px;
    background: rgba(255,255,255,0.25);
  }
  .contact { position: absolute; left: 520px; top: 50px; color: var(--white); }
  .contact-row { display: flex; align-items: flex-end; gap: 14px; margin-bottom: 24px; }
  .contact-row svg { width: 26px; height: 26px; flex: none; margin-bottom: 3px; }
  .contact-label { color: var(--sky); font-size: 22px; font-weight: 500; line-height: 1.1; }
  .contact-value { font-size: 26px; font-weight: 500; line-height: 1.15; }
  .contact-value .accent { color: var(--sky); }
  /* Back */
  .card-back {
    top: 626px;
    background: radial-gradient(circle at 50% 40%, var(--navy-light), var(--navy) 55%, var(--navy-deep));
  }
  .card-back .brand { top: 150px; flex-direction: column; gap: 14px; color: var(--ice); font-size: 96px; line-height: 1; }
  .card-back .brand-dot { width: 70px; height: 70px; }
  .brand-sub { font-size: 34px; letter-spacing: 6px; }
  .service-band {
    position: absolute; left: 0; right: 0; bottom: 40px; height: 66px;
    background: var(--lime);
    display: flex; align-items: center; justify-content: center;
    font-family: "Oswald", sans-serif; font-weight: 500; text-transform: uppercase;
    color: var(--navy); font-size: 28px; letter-spacing: 0.5px; gap: 14px;
  }
  .bullet { width: 8px; height: 8px; border-radius: 50%; background: var(--navy); }
</style>
</head>
<body>
  <section class="card card-front">
    <div class="brand"><span class="brand-dot"></span><span>Glintvale Window Cleaning</span></div>
    <div class="front-stripe"></div>
    <div class="front-panel">
      <div class="person">
        <div class="person-name">JOHN DOE</div>
        <div class="person-role">CEO | FOUNDER</div>
      </div>
      <div class="divider"></div>
      <div class="contact">
        <div class="contact-row">
          <svg viewBox="0 0 24 24" aria-hidden="true"><path fill="#2a9ad6" d="M6.6 10.8a15.1 15.1 0 0 0 6.6 6.6l2.2-2.2c.3-.3.7-.4 1-.2 1.1.4 2.3.6 3.6.6.6 0 1 .4 1 1V20c0 .6-.4 1-1 1A17 17 0 0 1 3 4c0-.6.4-1 1-1h3.5c.6 0 1 .4 1 1 0 1.3.2 2.5.6 3.6.1.3 0 .7-.2 1z"/></svg>
          <div>
            <div class="contact-label">Call or Text</div>
            <div class="contact-value">612-437-9158</div>
          </div>
        </div>
        <div class="contact-row">
          <svg viewBox="0 0 24 24" aria-hidden="true" fill="none" stroke="#2a9ad6" stroke-width="1.6"><circle cx="12" cy="12" r="9.5"/><ellipse cx="12" cy="12" rx="4.5" ry="9.5"/><path d="M2.5 12h19M4 7h16M4 17h16"/></svg>
          <div class="contact-value">www.<span class="accent">GlintvaleCo</span>.com</div>
        </div>
      </div>
    </div>
  </section>

  <section class="card card-back">
    <div class="brand">
      <span class="brand-dot"></span>
      <span>Glintvale</span>
      <span class="brand-sub">Window Cleaning</span>
    </div>
    <div class="service-band">
      <span>Window Cleaning</span><span class="bullet"></span>
      <span>Gutter Cleaning &amp; Covers</span><span class="bullet"></span>
      <span>Christmas Lighting</span>
    </div>
  </section>
</body>
</html>
```